Business card design needed

We are a manufacturing business based in Archerfield, Brisbane, Queensland. We Insulate airconditioning ductwork and also manufacture some duct.
Updates

Hi guys, thanks for all the responses, they are looking really great

I have attached a couple of better quality photos of the products we use or manufacture, they don't "need" to be used in the card but i thought it was worth uploading them

I will be picking the final card in the next couple of days

Thanks for the response.

I think this will be the last update but i have included what we do so it can be added to the back of a card.

Target Market(s)

Local contractors

Industry/Entity Type

Business

Contact Information for Business Card

Korrin Insulation
Mark Delaney
87 Tullamore Road
Brenmoor, QLD, 4117
mark@korrininsulation.example.com.au
Phone: 07 3914 2260

Requirements
Must have
• our logo which i have attached

Also, on the back of the card it would be nice to have what we do

-Duct lagging (internal and external)
-Manufacture of Z7 boxes
-Supply of glasswool, foam insulation, ductboard, foils, tapes & pins.

```html
<!DOCTYPE html>
<html lang="en">
<head>
<meta charset="utf-8">
<title>Korrin Insulation – Business Card</title>
<link href="https://fonts.googleapis.com/css2?family=Arimo:wght@400&display=swap" rel="stylesheet">
<style>
  :root {
    --orange: #e8791f;
    --ink: #1f1f1f;
    --charcoal: #3b3b3b;
    --band-deep: #e5843f;
    --band-pale: #fbeedd;
    --paper: #ffffff;
    --edge: #b9b9b9;
  }
  html, body {
    margin: 0;
    padding: 0;
    width: 1200px;
    height: 741px;
    overflow: hidden;
    background: var(--paper);
  }
  .card {
    position: relative;
    width: 1200px;
    height: 741px;
    box-sizing: border-box;
    border: 1px solid var(--edge);
    background: var(--paper);
    overflow: hidden;
    font-family: "Arimo", Arial, sans-serif;
  }
  .card__footer-band {
    position: absolute;
    left: 0;
    right: 0;
    bottom: 0;
    height: 96px;
    background: linear-gradient(90deg, var(--band-deep) 0%, #eeb07a 55%, var(--band-pale) 100%);
  }
  .brand {
    position: absolute;
    left: 52px;
    top: 98px;
    display: flex;
    align-items: center;
    gap: 18px;
  }
  .brand__square {
    width: 54px;
    height: 54px;
    background: var(--orange);
  }
  .brand__name {
    font-size: 50px;
    line-height: 1;
    color: var(--charcoal);
    white-space: nowrap;
  }
  .contact {
    position: absolute;
    right: 73px;
    top: 0;
    text-align: right;
    white-space: nowrap;
  }
  .contact__company {
    position: absolute;
    right: 8px;
    top: 88px;
    margin: 0;
    font-size: 48px;
    font-weight: 400;
    color: var(--orange);
  }
  .contact__person {
    position: absolute;
    right: 8px;
    top: 160px;
    margin: 0;
    font-size: 43px;
    font-weight: 400;
    color: var(--ink);
  }
  .contact__details {
    position: absolute;
    right: 0;
    top: 262px;
    margin: 0;
    font-size: 37px;
    line-height: 55px;
    color: var(--ink);
    font-style: normal;
  }
  .contact__label { color: var(--orange); }
</style>
</head>
<body>
<div class="card">
  <div class="card__footer-band" aria-hidden="true"></div>

  <div class="brand">
    <div class="brand__square"></div>
    <div class="brand__name">Korrin Insulation</div>
  </div>

  <div class="contact">
    <h1 class="contact__company">Korrin Insulation</h1>
    <h2 class="contact__person">Mark Delaney</h2>
    <address class="contact__details">
      87 Tullamore Road<br>
      Brenmoor, QLD, 4117<br>
      <span class="contact__label">E-mail:</span> mark@korrininsulation.example.com.au<br>
      <span class="contact__label">Phone:</span> 07 3914 2260
    </address>
  </div>
</div>
</body>
</html>
```